A4 Block Hour Agreement Brochure

We need a new Block Hour Agreement Brochure created as our current one lacks design and is ugly. The current block hour agreement brochure has been attached "pixelharbor.pdf".

We are looking at a modern brochure and have attached "Vellamore Private Cloud Plans.pdf" as an example.

It doesnt have to be the exact same design, but it must be the "Vellamore blue" theme.

Target Market(s)

Information Technology

Colors
0054AA
0677BA
7BADD7
CADEEF
E8F1F8

```html
<!DOCTYPE html>
<html lang="en">
<head>
<meta charset="utf-8">
<title>Block Hour Agreement – Vellamore Technologies</title>
<link href="https://fonts.googleapis.com/css2?family=Questrial&family=Poppins:wght@600&display=swap" rel="stylesheet">
<style>
  :root {
    --backdrop: #8a8a8a;
    --navy-deep: #07081f;
    --navy: #12134a;
    --earth-blue: #1d2a7a;
    --glow: #2f4fbf;
    --brand-blue: #0054AA;
    --ink-light: #ffffff;
    --ink-soft: #e8f1f8;
    --rule: #cadeef;
  }
  * { box-sizing: border-box; margin: 0; padding: 0; }
  html, body { width: 1199px; height: 1200px; overflow: hidden; }
  body {
    background: var(--backdrop);
    font-family: "Questrial", "Helvetica Neue", Arial, sans-serif;
    color: var(--ink-light);
  }
  .brochure {
    position: absolute;
    left: 174px; top: 0;
    width: 850px; height: 1200px;
    background: linear-gradient(180deg, var(--navy-deep) 0%, #0b0c2c 45%, var(--navy) 100%);
    overflow: hidden;
  }
  .earth-visual {
    position: absolute;
    left: -120px; top: 770px;
    width: 1090px; height: 900px;
    border-radius: 50%;
    background: radial-gradient(ellipse at 50% 20%, #2a3a9a 0%, var(--earth-blue) 30%, #141a55 60%, #0a0c2a 100%);
    box-shadow: 0 -18px 60px rgba(60, 90, 220, 0.55);
    opacity: 0.85;
  }
  .title {
    position: absolute; left: 53px; top: 62px;
    font-family: "Poppins", "Helvetica Neue", Arial, sans-serif;
    font-weight: 600; font-size: 54px; line-height: 71px;
    letter-spacing: -0.5px;
  }
  .brand-box {
    position: absolute; left: 474px; top: 49px;
    width: 376px; height: 102px;
    background: #fff;
    display: flex; align-items: center; justify-content: center; gap: 14px;
  }
  .brand-box .mark { width: 26px; height: 26px; background: var(--brand-blue); }
  .brand-box .name {
    font-family: "Questrial", Arial, sans-serif;
    font-size: 30px; color: var(--brand-blue); letter-spacing: 1px;
  }
  .overview { position: absolute; left: 53px; top: 262px; width: 740px; }
  .overview h2 {
    font-family: "Poppins", Arial, sans-serif; font-weight: 600;
    font-size: 24px; margin-bottom: 8px;
  }
  .overview p {
    font-size: 17px; line-height: 21.5px; color: var(--ink-soft);
    margin-bottom: 21px;
  }
  .terms { position: absolute; left: 53px; top: 578px; width: 740px; list-style: none; }
  .terms li {
    position: relative; padding-left: 40px;
    font-size: 17px; line-height: 21px; color: var(--ink-soft);
    margin-bottom: 7.5px;
  }
  .terms svg { position: absolute; left: 0; top: 4px; width: 14px; height: 14px; }
  .pricing { position: absolute; left: 336px; top: 806px; width: 460px; }
  .pricing h2 {
    font-family: "Poppins", Arial, sans-serif; font-weight: 600;
    font-size: 24px; text-align: center; margin-bottom: 14px;
    padding-right: 30px;
  }
  .price-table { width: 460px; border-collapse: collapse; font-size: 15px; }
  .price-table th, .price-table td {
    border: 2px solid var(--rule); height: 32px; padding: 0 10px;
  }
  .price-table th { background: #fff; color: #111; font-weight: normal; text-align: center; }
  .price-table td { text-align: right; color: var(--ink-soft); }
  .price-table td:first-child { text-align: center; }
  .fine-print {
    position: absolute; left: 53px; top: 1094px; width: 760px;
    font-size: 16.5px; line-height: 20px; color: var(--ink-soft);
  }
</style>
</head>
<body>
<main class="brochure">
  <div class="earth-visual" role="img" aria-label="Night view of the Earth with glowing network connections"></div>

  <h1 class="title">Block Hour<br>Agreement</h1>

  <div class="brand-box">
    <span class="mark"></span>
    <span class="name">VELLAMORE</span>
  </div>

  <section class="overview">
    <h2>Overview</h2>
    <p>Vellamore Technologies offers the Block Time Service Agreement at a discounted hourly rate for clients who need consistent support throughout a period of time. A block time agreement lets you pre-pay for services and call upon them as needed, this allows for easy accounting and easy support.</p>
    <p>Our Block Time Service Agreement can be used for all non-project related work, please ask your Vellamore representative for more details.</p>
    <p>Block hours are not covered under a Service Level Agreement (SLA) and are best effort, while we endeavor to always provide prompt service to our customers in some situations such as a service disruption, it may not always be possible to attend straight away.</p>
  </section>

  <ul class="terms">
    <li><svg viewBox="0 0 14 14"><rect x="1" y="3" width="10" height="10" fill="none" stroke="#fff" stroke-width="1.2"/><path d="M3 7l3 3 7-8" fill="none" stroke="#fff" stroke-width="1.5"/></svg>Block hours do not rollover</li>
    <li><svg viewBox="0 0 14 14"><rect x="1" y="3" width="10" height="10" fill="none" stroke="#fff" stroke-width="1.2"/><path d="M3 7l3 3 7-8" fill="none" stroke="#fff" stroke-width="1.5"/></svg>There is no set usage per week.</li>
    <li><svg viewBox="0 0 14 14"><rect x="1" y="3" width="10" height="10" fill="none" stroke="#fff" stroke-width="1.2"/><path d="M3 7l3 3 7-8" fill="none" stroke="#fff" stroke-width="1.5"/></svg>Project services cannot be used with block time.</li>
    <li><svg viewBox="0 0 14 14"><rect x="1" y="3" width="10" height="10" fill="none" stroke="#fff" stroke-width="1.2"/><path d="M3 7l3 3 7-8" fill="none" stroke="#fff" stroke-width="1.5"/></svg>Time is billed in 0.5 hour increments with a minimum of 1 hour for onsite callouts.</li>
    <li><svg viewBox="0 0 14 14"><rect x="1" y="3" width="10" height="10" fill="none" stroke="#fff" stroke-width="1.2"/><path d="M3 7l3 3 7-8" fill="none" stroke="#fff" stroke-width="1.5"/></svg>Hours must be used within 12 months of purchase</li>
    <li><svg viewBox="0 0 14 14"><rect x="1" y="3" width="10" height="10" fill="none" stroke="#fff" stroke-width="1.2"/><path d="M3 7l3 3 7-8" fill="none" stroke="#fff" stroke-width="1.5"/></svg>Hours must be used during standard business hours 8:30am-5pm AWST. After hours is charged at double time.</li>
  </ul>

  <section class="pricing">
    <h2>Agreement Types</h2>
    <table class="price-table">
      <thead>
        <tr><th>Hours</th><th>Hourly Rate</th><th>Cost (Ex GST)</th></tr>
      </thead>
      <tbody>
        <tr><td>1</td><td>$270.00</td><td>$265.00</td></tr>
        <tr><td>10</td><td>$240.00</td><td>$2,400.00</td></tr>
        <tr><td>20</td><td>$225.00</td><td>$4,500.00</td></tr>
        <tr><td>35</td><td>$220.00</td><td>$7,700.00</td></tr>
        <tr><td>50</td><td>$210.00</td><td>$10,500.00</td></tr>
      </tbody>
    </table>
  </section>

  <p class="fine-print">By engaging with Vellamore in goods/services you agree to our Terms and Conditions available at https://www.vellamoretech.com.au/t&amp;c</p>
</main>
</body>
</html>
```